Webdesign für Physiotherapie
Zielgruppe
Physiotherapie unter ganzheitlichen oder umfangreicheren Gesichtspunkten.
ANLAGE BEACHTEN!
Aufgabenstellung
Siehe Anlage!

```html
<!DOCTYPE html>
<html lang="de">
<head>
<meta charset="utf-8">
<title>Über mich – DK3 Physiotherapie</title>
<link href="https://fonts.googleapis.com/css2?family=Raleway:ital,wght@0,300;0,400;0,600;0,700;1,300&family=Schoolbell&display=swap" rel="stylesheet">
<style>
:root{
  --gray:#666666;
  --gray-dark:#5a5a5a;
  --yellow:#dbb12a;
  --yellow-soft:#e4c96f;
  --red:#e03e24;
  --text:#6b6b6b;
  --white:#ffffff;
  --hand:'Schoolbell',cursive;
  --sans:'Raleway',sans-serif;
}
*{margin:0;padding:0;box-sizing:border-box}
html,body{width:1200px;height:2310px;overflow:hidden;background:var(--white)}
body{position:relative;font-family:var(--sans);color:var(--text);font-weight:300}
.abs{position:absolute}
.hand{font-family:var(--hand);font-weight:400}

/* nav */
.nav{left:0;top:0;width:1200px;height:49px;background:var(--gray)}
.brand{left:263px;top:13px;color:var(--yellow);font-weight:700;font-size:16px;display:flex;align-items:center;gap:6px}
.brand i{width:10px;height:10px;border-radius:50%;background:var(--yellow);display:block}
.nav-link{top:17px;color:#f2f2f2;font-size:13.5px;font-weight:400}
.nav-link.active{font-weight:700;color:#fff}
.nav-underline{left:713px;top:45px;width:153px;height:4px;background:var(--red)}
.tagline{left:0;top:49px;width:1200px;height:27px;background:var(--yellow);text-align:center;font-size:11px;line-height:27px;color:#6d5a1c}

/* hero */
.hero{left:0;top:76px;width:1200px;height:259px;background:linear-gradient(90deg,#5c5c5c 0%,#6a6a6a 45%,#cfcfcf 70%,#efefef 100%)}
.hero-kicker{left:263px;top:170px;color:#fff;font-size:17px}
.hero-title{left:263px;top:192px;color:#fff;font-size:32px;font-weight:600}
.hero-title span{color:var(--yellow)}
.portrait{left:656px;top:222px;width:282px;height:282px;border-radius:50%;background:radial-gradient(circle at 50% 40%,#d8d8d8,#9a9a9a 70%,#5e5e5e);box-shadow:0 4px 14px rgba(0,0,0,.15)}

/* intro card */
.hello{left:737px;top:471px;width:157px;height:145px;background:#fff;border-radius:4px;box-shadow:0 2px 10px rgba(0,0,0,.12);padding:30px 16px 0 20px;font-size:12px;line-height:15.5px}
.hello b{font-weight:600;color:#5a5a5a}
.hello small{display:block;margin-top:12px;font-size:8px;line-height:10px;font-style:italic}
.smile{left:852px;top:483px}
.doodle{left:676px;top:450px}

/* letter */
.greet{left:263px;top:398px;font-size:26px;color:#666}
.line{height:3px;background:var(--yellow)}
.letter{left:263px;top:466px;width:395px;font-size:15.5px;line-height:21.9px;font-weight:400;color:#777}
.letter p{margin-bottom:21.9px}
.sign{left:263px;top:866px;font-size:17px;color:#666}

/* conditions */
.band{left:0;top:967px;width:1200px;height:531px;background:var(--yellow)}
.cond-title{left:263px;top:1002px;color:#fff;font-size:21px;line-height:29px}
.cond-text{left:331px;top:1100px;width:270px;color:#fff;font-size:13.5px;line-height:21.9px;font-weight:400}
.cond-text p{margin-bottom:21.9px}
.tick{left:281px}

/* focus card */
.focus{left:653px;top:868px;width:242px;height:452px;background:#fff;border-radius:5px;box-shadow:0 2px 10px rgba(0,0,0,.1)}
.focus-title{left:0;top:42px;width:242px;text-align:center;font-size:16.5px;line-height:20px;color:#666}
.focus-line{left:72px;top:105px;width:98px;height:3px;background:var(--red)}
.focus-list{left:30px;top:138px;width:200px;list-style:none;font-size:13.5px;line-height:25.6px;font-weight:400;color:#666}
.focus-list li{position:relative;padding-left:16px}
.focus-list li::before{content:"•";position:absolute;left:2px;font-size:9px;color:#888}
.clip{left:758px;top:852px}

/* method */
.method-kicker{left:0;top:1572px;width:1200px;text-align:center;font-size:17px;color:#666}
.method-title{left:0;top:1598px;width:1200px;text-align:center;font-size:29px;line-height:32px;font-weight:700;color:#666}
.method-title span{color:var(--yellow)}
.method-line{left:552px;top:1686px;width:98px}
.method-text{left:325px;top:1716px;width:550px;text-align:center;font-size:15.5px;line-height:21.9px;font-weight:400;color:#777}
.method-text b{color:var(--yellow);font-weight:700}
.btn{left:524px;top:1854px;width:152px;height:45px;border-radius:23px;background:var(--red);color:#fff;font-weight:700;font-size:15.5px;text-align:center;line-height:45px;box-shadow:0 3px 8px rgba(224,62,36,.3)}

/* footer */
.footer{left:0;top:2033px;width:1200px;height:230px;background:linear-gradient(90deg,var(--yellow-soft) 0%,#e4c96f 50%,#c9a97a 70%,#8d8a86 100%)}
.up{left:833px;top:1975px;width:104px;height:104px;border-radius:50%;background:#e4c96f;text-align:center;color:#fff;font-size:13px}
.find{left:263px;top:2051px;font-size:21px;color:#666}
.address{left:263px;top:2113px;font-size:12.5px;line-height:18.8px;color:#7a6a3a;font-weight:400}
.foot-brand{left:545px;top:2118px;width:110px;height:60px;display:flex;align-items:center;justify-content:center;gap:8px;color:#fff;font-size:30px;font-weight:700}
.foot-brand i{width:14px;height:14px;border-radius:50%;background:#fff;display:block}
.bottom{left:0;top:2263px;width:1200px;height:47px;background:var(--gray);color:#fff}
.bottom a{position:absolute;top:17px;font-size:10.5px;font-weight:700;color:#fff;text-decoration:none}
.copy{position:absolute;left:784px;top:18px;font-size:8.5px;font-weight:400}
</style>
</head>
<body>

<header class="abs nav">
  <div class="abs brand"><i></i>DK3</div>
  <a class="abs nav-link" style="left:550px">Home</a>
  <a class="abs nav-link" style="left:622px">Über mich</a>
  <a class="abs nav-link active" style="left:713px">DK3 Behandlungssäulen</a>
  <a class="abs nav-link" style="left:893px">Kontakt</a>
  <div class="abs nav-underline"></div>
</header>
<div class="abs tagline hand">Ihre DK3 Physiotherapie Privatpraxis in Lindenau</div>

<section class="abs hero" role="img" aria-label="Foto: anatomische Skizze einer Wirbelsäule auf Papier"></section>
<div class="abs hero-kicker hand">Daniel Kerstenhof</div>
<h1 class="abs hero-title">Über <span>mich</span></h1>
<div class="abs portrait" role="img" aria-label="Porträtfoto des Physiotherapeuten"></div>

<svg class="abs doodle" width="60" height="110" viewBox="0 0 60 110" aria-hidden="true">
  <path d="M40 104 C14 80 4 56 18 26" fill="none" stroke="var(--yellow)" stroke-width="3" stroke-linecap="round"/>
  <path d="M40 84 C24 66 18 42 30 8" fill="none" stroke="var(--red)" stroke-width="3" stroke-linecap="round"/>
  <path d="M22 14 L30 6 L34 18" fill="none" stroke="var(--red)" stroke-width="3" stroke-linecap="round" stroke-linejoin="round"/>
</svg>
<div class="abs hello">Hey, ich bin<br><b>Daniel Kerstenhof.</b><br>Ich freue mich, Sie kennenzulernen.<small>leidenschaftlicher Physiotherapeut &amp; sektoraler Heilpraktiker</small></div>
<svg class="abs smile" width="26" height="26" viewBox="0 0 26 26" aria-hidden="true">
  <circle cx="13" cy="13" r="11" fill="none" stroke="var(--red)" stroke-width="1.8"/>
  <path d="M7 11 q2 -2 4 0 M15 11 q2 -2 4 0 M7.5 15 q5.5 5 11 0" fill="none" stroke="var(--red)" stroke-width="1.6" stroke-linecap="round"/>
</svg>

<h2 class="abs greet hand">Liebe Patienten,</h2>
<div class="abs line" style="left:262px;top:441px;width:98px"></div>
<div class="abs letter">
  <p>Lorem ipsum dolor sit amet, consectetuer adipiscing elit. Phasellus hendrerit. Pellentesque aliquet nibh nec urna. In nisi neque, aliquet vel, dapibus id, mattis vel, nisi. Sed pretium, ligula sollicitudin laoreet viverra, tortor libero sodales leo, eget blandit nunc tortor eu nibh. Nullam mollis. Ut justo. Suspendisse potenti.</p>
  <p>Sed egestas, ante et vulputate volutpat, eros pede semper est, vitae luctus metus libero eu augue. Morbi purus libero, faucibus adipiscing, commodo quis, gravida id, est. Sed lectus. Praesent elementum hendrerit tortor. Sed semper lorem at felis. Vestibulum volutpat, lacus a ultrices sagittis, mi neque euismod dui, eu pulvinar nunc sapien ornare nisl. Phasellus pede arcu, dapibus eu, fermentum et, dapibus sed, urna.</p>
  <p style="margin:0">Ich freue mich, Sie kennenzulernen!</p>
</div>
<div class="abs sign hand">Ihre Daniel Kerstenhof</div>

<section class="abs band"></section>
<h2 class="abs cond-title hand">Mit diesen Erkrankungen sind Sie<br>bestens bei mir aufgehoben:</h2>
<svg class="abs tick" style="top:1101px" width="28" height="26" viewBox="0 0 28 26" aria-hidden="true"><rect x="1" y="6" width="18" height="18" rx="3" fill="none" stroke="#fff" stroke-width="1.6"/><path d="M5 14 L10 20 L26 2" fill="none" stroke="var(--red)" stroke-width="3" stroke-linecap="round" stroke-linejoin="round"/></svg>
<svg class="abs tick" style="top:1186px" width="28" height="26" viewBox="0 0 28 26" aria-hidden="true"><rect x="1" y="6" width="18" height="18" rx="3" fill="none" stroke="#fff" stroke-width="1.6"/><path d="M5 14 L10 20 L26 2" fill="none" stroke="var(--red)" stroke-width="3" stroke-linecap="round" stroke-linejoin="round"/></svg>
<svg class="abs tick" style="top:1293px" width="28" height="26" viewBox="0 0 28 26" aria-hidden="true"><rect x="1" y="6" width="18" height="18" rx="3" fill="none" stroke="#fff" stroke-width="1.6"/><path d="M5 14 L10 20 L26 2" fill="none" stroke="var(--red)" stroke-width="3" stroke-linecap="round" stroke-linejoin="round"/></svg>
<div class="abs cond-text">
  <p>Morbi in sem quis dui placerat ornare. Pellentesque odio nisi, euismod in, pharetra a, ultricies in, diam. Sed arcu. Cras consequat</p>
  <p>Praesent dapibus, neque id cursus faucibus, tortor neque egestas augue, eu vulputate magna eros eu erat. Aliquam erat volutpat. Nam dui mi, tincidunt quis, accumsan porttitor, facilisis luctus, metus.</p>
  <p>Phasellus ultrices nulla quis nibh. Quisque a lectus. Donec consectetuer ligula vulputate sem tristique cursus. Nam nulla quam, gravida non, commodo a, sodales sit amet, nisi.</p>
</div>

<aside class="abs focus">
  <h3 class="abs focus-title hand">Meine Schwerpunkte<br>im Überblick</h3>
  <div class="abs focus-line"></div>
  <ul class="abs focus-list">
    <li>Manuelle Therapie</li>
    <li>Krankengymnastik</li>
    <li>Cranio Sacrale Therapie</li>
    <li>Kiefergelenksbehandlung</li>
    <li>Wärme- und Kälte<br>Therapie</li>
    <li>Massage</li>
    <li>Kinesio-Taping</li>
    <li>Lymphdrainage</li>
    <li>Elektrotherapie &amp;<br>Ultraschall</li>
  </ul>
</aside>
<svg class="abs clip" width="32" height="30" viewBox="0 0 32 30" aria-hidden="true">
  <path d="M26 24 L9 9 a4 4 0 0 1 6 -5 L29 17 a2.5 2.5 0 0 1 -4 3 L13 9" fill="none" stroke="var(--red)" stroke-width="2" stroke-linecap="round"/>
</svg>

<div class="abs method-kicker hand">Meine Behandlungsmethodik</div>
<h2 class="abs method-title">Ich arbeite nach<br>dem <span>DK3</span> Prinzip</h2>
<div class="abs line method-line"></div>
<p class="abs method-text"><b>DK3</b> ist eine Kombination aus den Anfangsbuchstaben meines Vor- und Nachnamens, Daniel Kerstenhof. Die 3 steht für die 3 Betrachtungsweisen, nach denen ich Befunde oder besser gesagt meinen Therapieleitfaden gestalte, nämlich die 3 Säulen der Behandlung.</p>
<a class="abs btn">Mehr dazu</a>

<footer class="abs footer" role="img" aria-label="Foto: Therapeut behandelt das Knie eines Patienten in der Praxis"></footer>
<div class="abs up hand">
  <svg width="24" height="34" viewBox="0 0 24 34" style="margin-top:22px" aria-hidden="true"><path d="M12 2 L22 16 H15 V32 H9 V16 H2 Z" fill="var(--red)"/></svg>
  <div style="margin-top:2px">Nach oben</div>
</div>
<h2 class="abs find hand">Hier finden Sie mich!</h2>
<div class="abs line" style="left:263px;top:2092px;width:98px;background:var(--red)"></div>
<address class="abs address" style="font-style:normal">
  Daniel Kerstenhof<br>Physiotherapeut<br><br>Ahornweg 7<br>34567 Lindenau<br>04567 3021880
</address>
<div class="abs foot-brand"><i></i>DK3</div>

<div class="abs bottom">
  <a style="left:263px">Datenschutz</a>
  <a style="left:361px">Impressum</a>
  <span class="copy">Copyright 2023 © Daniel Kerstenhof</span>
</div>

</body>
</html>
```